Professional Business Cards

We need a nice looking, profession and modern business card for our new company. Our logo is attatched

Target Market(s)

Young Professionals

Industry/Entity Type

Financial

Contact Information for Business Card

FRONT

Morvane Tally Pty Ltd
Level 22, Halden Court, 48 Wirrapool St
Sydney NSW 2000
ABN : 57 304 918 226

Derek Wallis - Chief Operations Officer
P : 02 7153 2819
M: 0418 395 207
derek@morvanetally,com

BACK

- Cryptocurrency Exchange Services
- Cryptocurrency Mining Operations
- Cryptocurrency Investment Fund Offering

Font styles to use
Sans Serif

Colors
0255a3
9d9d9d

```html
<!DOCTYPE html>
<html lang="en">
<head>
<meta charset="utf-8">
<title>Morvane Tally – Business Card</title>
<link rel="stylesheet" href="https://fonts.googleapis.com/css2?family=Roboto:wght@400;500;700&family=Roboto+Condensed:wght@500;700&display=swap">
<style>
  :root {
    --brand-blue: #0255a3;
    --brand-grey: #9d9d9d;
    --stage: #2a2a2a;
    --card-white: #f3f3f3;
    --text-dark: #4a4a4a;
    --text-mid: #7a7a7a;
    --rule: #9a9a9a;
  }
  * { box-sizing: border-box; margin: 0; padding: 0; }
  html, body { width: 1200px; height: 960px; overflow: hidden; }
  body {
    position: relative;
    background: var(--stage);
    font-family: "Roboto", Arial, sans-serif;
  }
  .card {
    position: absolute;
    width: 600px;
    height: 342px;
    overflow: hidden;
  }
  /* Front */
  .card--front { left: 314px; top: 113px; background: var(--card-white); }
  .front-brand {
    position: absolute;
    left: 52px; top: 150px;
    display: flex; align-items: center; gap: 12px;
  }
  .brand-square {
    width: 26px; height: 26px;
    background: var(--brand-blue);
  }
  .brand-name {
    font-family: "Roboto", Arial, sans-serif;
    font-weight: 700;
    font-size: 26px;
    letter-spacing: 1px;
    color: var(--brand-blue);
    line-height: 1;
  }
  .divider {
    position: absolute;
    left: 325px; top: 62px;
    width: 2px; height: 228px;
    background: var(--rule);
  }
  .contact {
    position: absolute;
    left: 351px; top: 64px;
    color: var(--text-dark);
    font-size: 14.5px;
    line-height: 18px;
  }
  .contact__name {
    font-family: "Roboto Condensed", Arial, sans-serif;
    font-weight: 700;
    font-size: 22px;
    line-height: 26px;
    color: var(--brand-blue);
    text-transform: uppercase;
  }
  .contact__role { color: var(--text-mid); font-size: 15px; margin-bottom: 8px; }
  .contact__company { font-weight: 700; }
  .contact__lines { list-style: none; margin-top: 8px; }
  .contact__lines li { display: flex; align-items: center; gap: 8px; height: 19px; }
  .contact__lines svg { width: 14px; height: 14px; fill: var(--brand-blue); flex: none; }
  .contact__abn { margin-top: 7px; }
  .front-band { position: absolute; left: 0; bottom: 0; width: 600px; height: 20px; }

  /* Back */
  .card--back { left: 311px; top: 472px; background: var(--brand-blue); }
  .back-brand {
    position: absolute;
    left: 0; right: 0; top: 140px;
    display: flex; justify-content: center; align-items: center; gap: 16px;
  }
  .back-brand .brand-square { width: 40px; height: 40px; background: #ffffff; }
  .back-brand .brand-name { color: #ffffff; font-size: 44px; }
  .services {
    position: absolute;
    left: 0; right: 0; top: 274px;
    text-align: center;
    color: #ffffff;
    font-size: 14.5px;
    line-height: 18px;
  }
  .services__sep { font-size: 10px; vertical-align: 2px; padding: 0 4px; }
</style>
</head>
<body>

<section class="card card--front" aria-label="Business card front">
  <div class="front-brand">
    <span class="brand-square"></span>
    <span class="brand-name">MORVANE TALLY</span>
  </div>

  <div class="divider"></div>

  <div class="contact">
    <p class="contact__name">Derek Wallis</p>
    <p class="contact__role">Chief Operations Officer</p>
    <p class="contact__company">Morvane Tally Pty Ltd</p>
    <p>Level 22, Halden Court</p>
    <p>48 Wirrapool St</p>
    <p>Sydney NSW 2000</p>
    <ul class="contact__lines">
      <li>
        <svg viewBox="0 0 24 24" aria-hidden="true"><path d="M6.6 10.8c1.4 2.8 3.8 5.1 6.6 6.6l2.2-2.2c.3-.3.7-.4 1-.2 1.1.4 2.3.6 3.6.6.6 0 1 .4 1 1V20c0 .6-.4 1-1 1C10.6 21 3 13.4 3 4c0-.6.4-1 1-1h3.5c.6 0 1 .4 1 1 0 1.3.2 2.5.6 3.6.1.3 0 .7-.2 1z"/></svg>
        <span>02 7153 2819</span>
      </li>
      <li>
        <svg viewBox="0 0 24 24" aria-hidden="true"><path d="M7 1h10c1.1 0 2 .9 2 2v18c0 1.1-.9 2-2 2H7c-1.1 0-2-.9-2-2V3c0-1.1.9-2 2-2zm0 3v14h10V4H7zm5 15.5a1.2 1.2 0 1 0 0 2.4 1.2 1.2 0 0 0 0-2.4z"/></svg>
        <span>0418 395 207</span>
      </li>
      <li>
        <svg viewBox="0 0 24 24" aria-hidden="true"><path d="M2 5h20v14H2V5zm2 2v.5l8 5 8-5V7H4zm0 2.9V17h16V9.9l-8 5-8-5z"/></svg>
        <span>derek@morvanetally.com</span>
      </li>
    </ul>
    <p class="contact__abn">ABN : 57 304 918 226</p>
  </div>

  <svg class="front-band" viewBox="0 0 600 20" preserveAspectRatio="none" aria-hidden="true">
    <polygon points="0,0 388,0 382,20 0,20" fill="var(--brand-blue)"/>
    <polygon points="393,0 600,0 600,20 387,20" fill="var(--brand-grey)"/>
  </svg>
</section>

<section class="card card--back" aria-label="Business card back">
  <div class="back-brand">
    <span class="brand-square"></span>
    <span class="brand-name">MORVANE TALLY</span>
  </div>
  <div class="services">
    <p>Cryptocurrency Exchange Services<span class="services__sep">◆</span>Cryptocurrency Mining Operations</p>
    <p>Cryptocurrency Investment Fund Offering</p>
  </div>
</section>

</body>
</html>
```